Tiles & Tonic - Promo Card

This is my first go at this... but I need some Business Card sized promotional material that we can hand out to customers at our retail store.
The promotional cards are designed to drive traffic for specific areas of our business, at specific times. We often staple them to customer receipts, but also will be handing them out to employees of major retailers as preferred customer cards for specific periods of time.
======================================================
Video Games:
(Standard) Tiles & Tonic VIP Customer Card
(Editable Text) On _________ receive 10% off all video game purchases
I want the "Editable Text" to allow us to easily change the criteria of the promo, or the date of the promo. Basically I am looking for a template that I can quickly send to the printshop when we have an idea.
I have some graphics with out logo, and past billboard we have used which could be used to see logo/colour (Do not use dog from billboard image). If we like the work there is a relatively significant amount of additional design work for signage, display cards, and the like around the store.
I have a .PSD file of our billboard... but it is 39MB and the software will not allow me to upload anything beyond 30MB. So I have attached a low res JPG. It should give you an idea of who we are though, the designer was from Winnipeg and well... you'll see.
For reference our website is: www.tilestonic.example
Target Market(s)
18-45 (male/female), low->midupper income, highschool->university education
Industry/Entity Type
Software
Look and feel
Each slider illustrates characteristics of the customer's brand and the style your logo design should communicate.

```html
<!DOCTYPE html>
<html lang="en">
<head>
<meta charset="utf-8">
<title>Tiles &amp; Tonic – Promo Card</title>
<link rel="stylesheet" href="https://fonts.googleapis.com/css2?family=Oswald:wght@500;700&family=Nunito:wght@800;900&display=swap">
<style>
  :root {
    --bg: #2b2b2d;
    --yellow: #f7e21e;
    --slate: #3f5560;
    --white: #ffffff;
    --panel: #e8e8e8;
    --ink: #2f434d;
  }
  * { box-sizing: border-box; margin: 0; padding: 0; }
  html, body { width: 1200px; height: 900px; overflow: hidden; background: var(--bg); }
  .canvas { position: relative; width: 1200px; height: 900px; }

  .card {
    position: absolute;
    width: 600px; height: 343px;
    background: var(--yellow);
    overflow: hidden;
    box-shadow: 0 10px 30px rgba(0,0,0,.45);
  }

  /* ---------- Promo side ---------- */
  .card--promo { left: 300px; top: 60px; }
  .promo__band {
    position: absolute; left: 0; bottom: 0; width: 100%; height: 62px;
    background: var(--slate);
    border-top: 6px solid var(--white);
  }
  .promo__stripes { position: absolute; left: 0; top: 0; }
  .promo__url {
    position: absolute; left: 110px; top: 9px;
    font-family: "Oswald", sans-serif; font-weight: 700;
    font-size: 30px; letter-spacing: .5px; color: var(--yellow);
  }
  .promo__category {
    position: absolute; right: 30px; top: 26px;
    font-family: "Oswald", sans-serif; font-weight: 700;
    font-size: 34px; color: var(--ink); letter-spacing: .5px;
  }
  .promo__field {
    position: absolute; right: 30px; top: 86px;
    width: 196px; height: 150px;
    background: var(--panel); border-radius: 10px;
    display: flex; align-items: center; justify-content: center; gap: 10px;
    font-family: "Oswald", sans-serif; font-weight: 500; font-size: 20px; color: var(--ink);
  }
  .promo__blank { width: 110px; border-bottom: 2px solid var(--ink); height: 22px; }
  .promo__offer {
    position: absolute; left: 26px; top: 30px;
    width: 330px; padding: 10px 20px 14px;
    background: var(--slate); border-radius: 26px;
    font-family: "Oswald", sans-serif; font-weight: 700; color: var(--white);
    text-align: center; line-height: .95;
  }
  .promo__lead { font-size: 52px; }
  .promo__amount { font-size: 104px; color: var(--yellow); letter-spacing: 2px; }
  .promo__detail { font-size: 20px; letter-spacing: 1px; margin-top: 4px; }
  .promo__closing { font-size: 44px; letter-spacing: 1px; }

  /* ---------- Name side ---------- */
  .card--brand { left: 300px; top: 480px; }
  .brand__top {
    position: absolute; left: 0; top: 0; width: 100%; height: 26px;
    background: var(--slate); border-bottom: 6px solid var(--white);
  }
  .brand__bottom {
    position: absolute; left: 0; bottom: 0; width: 100%; height: 60px;
    background: var(--slate); border-top: 6px solid var(--white);
  }
  .brand__stripes { position: absolute; right: 0; top: 0; }
  .brand__lockup {
    position: absolute; left: 0; right: 0; top: 98px;
    text-align: center;
  }
  .brand__name {
    font-family: "Nunito", sans-serif; font-weight: 900;
    font-size: 62px; color: var(--slate); letter-spacing: 1px;
  }
  .brand__tagline {
    margin-top: 6px;
    font-family: "Nunito", sans-serif; font-weight: 900;
    font-size: 30px; color: var(--slate);
  }
</style>
</head>
<body>
<main class="canvas">

  <section class="card card--promo" aria-label="Promotional side">
    <div class="promo__category">VIDEO GAMES</div>
    <div class="promo__field"><span>ON</span><span class="promo__blank"></span></div>
    <div class="promo__offer">
      <div class="promo__lead">receive</div>
      <div class="promo__amount">10%</div>
      <div class="promo__detail">OFF ALL VIDEO GAME</div>
      <div class="promo__closing">PURCHASES</div>
    </div>
    <div class="promo__band">
      <svg class="promo__stripes" width="100" height="56" viewBox="0 0 100 56">
        <g stroke="#f7e21e" stroke-width="3">
          <line x1="10" y1="56" x2="50" y2="0"/>
          <line x1="24" y1="56" x2="64" y2="0"/>
          <line x1="38" y1="56" x2="78" y2="0"/>
          <line x1="52" y1="56" x2="92" y2="0"/>
        </g>
      </svg>
      <div class="promo__url">www.tilestonic.example</div>
    </div>
  </section>

  <section class="card card--brand" aria-label="Name side">
    <div class="brand__top"></div>
    <div class="brand__lockup">
      <div class="brand__name">TILES &amp; TONIC</div>
      <div class="brand__tagline">The Deals are Here!</div>
    </div>
    <div class="brand__bottom">
      <svg class="brand__stripes" width="220" height="54" viewBox="0 0 220 54">
        <g stroke="#f7e21e" stroke-width="3">
          <line x1="20" y1="54" x2="56" y2="0"/>
          <line x1="32" y1="54" x2="68" y2="0"/>
          <line x1="44" y1="54" x2="80" y2="0"/>
        </g>
      </svg>
    </div>
  </section>

</main>
</body>
</html>
```